My company is throwing a party. The name is 70/30 (70% Reggae & 30% Whatever Comes)

I seek a flyer that shows this will be a very elegant, upscale event and at the same time high energy, great reggae music and dancing.

I need this flyer to be 650 pixels wide & any length, High resolution (1MB) for printing on a 4" x 6" flyer.

Target Market(s)

Fans of reggae music

Industry/Entity Type

Printing

Requirements
Must have
• Lumen Harbor Holdings Presents:
70/30
Upscale Reggae Soiree
70% Reggae - 30% Whatever Comes

Saturday May 4th, 10pm - 3am

The Copperloft: 418 1/2 North Callow St, OKC

Dress to impress! We reserve the right to refuse entry

Free Entry: 1st 50 Ladies On VIP Guestlist - Discounted Early Bird Online Tickets - For Bottle Service Reservation: http://islandnights.ticketvoro.com

More info? 405-617-2958

```html
<!DOCTYPE html>
<html lang="en">
<head>
<meta charset="utf-8">
<title>70/30 Upscale Reggae Soiree</title>
<link rel="stylesheet" href="https://fonts.googleapis.com/css2?family=Poiret+One&display=swap">
<style>
  :root {
    --green-deep: #123f0c;
    --green: #2f7a1d;
    --green-bright: #4a9a2a;
    --gold: #d4a72a;
    --gold-light: #e6be45;
    --gold-dark: #9c7614;
    --cream: #f4e594;
    --ink: #2a1e08;
    --skin-light: #8a5428;
    --skin-dark: #2a1409;
  }
  html, body {
    margin: 0;
    padding: 0;
    width: 867px;
    height: 1200px;
    overflow: hidden;
    background: var(--green-deep);
  }
  .flyer {
    display: block;
    width: 867px;
    height: 1200px;
  }
  .flyer text {
    font-family: "Poiret One", "Josefin Sans", sans-serif;
    font-weight: 400;
  }
  .on-band {
    fill: var(--cream);
    stroke: var(--ink);
    stroke-width: 2.2px;
    paint-order: stroke;
    stroke-linejoin: round;
  }
  .headline-number {
    fill: var(--cream);
    stroke: var(--ink);
    stroke-width: 3.5px;
    paint-order: stroke;
    stroke-linejoin: round;
  }
  .on-green { fill: var(--cream); }
  .brand-name { fill: var(--gold-light); }
  .contact { fill: var(--cream); }
</style>
</head>
<body>
<svg class="flyer" viewBox="0 0 650 900" preserveAspectRatio="none" xmlns="http://www.w3.org/2000/svg">
  <defs>
    <radialGradient id="field" cx="50%" cy="45%" r="75%">
      <stop offset="0" stop-color="var(--green-bright)"/>
      <stop offset="0.6" stop-color="var(--green)"/>
      <stop offset="1" stop-color="var(--green-deep)"/>
    </radialGradient>
    <linearGradient id="band" x1="0" y1="0" x2="1" y2="1">
      <stop offset="0" stop-color="var(--gold-dark)"/>
      <stop offset="0.45" stop-color="var(--gold-light)"/>
      <stop offset="1" stop-color="var(--gold)"/>
    </linearGradient>
    <radialGradient id="portrait-tone" cx="60%" cy="45%" r="60%">
      <stop offset="0" stop-color="var(--skin-light)"/>
      <stop offset="0.7" stop-color="var(--skin-dark)"/>
      <stop offset="1" stop-color="var(--skin-dark)" stop-opacity="0.6"/>
    </radialGradient>
  </defs>

  <rect class="field" width="650" height="900" fill="url(#field)"/>

  <path class="portrait" role="img" aria-label="Painted portrait of a reggae singer, hand to chin"
        d="M590,170 L650,150 L650,820 C600,810 550,760 520,690 C480,600 450,480 480,380 C510,290 545,210 590,170 Z"
        fill="url(#portrait-tone)"/>

  <polygon class="band band-falling" points="-66,0 170,0 650,658 650,900 591,900 -66,0"/>
  <polygon class="band band-falling-fill" points="-66,0 170,0 650,658 650,900 591,900 0,90 0,0" fill="url(#band)"/>
  <polygon class="band band-rising" points="556,0 742,0 121,900 -96,900 -96,900" fill="url(#band)"/>

  <g class="brand">
    <circle cx="355" cy="44" r="13" fill="var(--gold-light)"/>
    <text class="brand-name" x="355" y="92" font-size="28" text-anchor="middle">Lumen Harbor</text>
    <text class="brand-name" x="355" y="120" font-size="24" text-anchor="middle">Holdings</text>
    <text class="brand-name" x="385" y="162" font-size="26" text-anchor="middle">presents</text>
  </g>

  <text class="headline-number" transform="translate(233,269) rotate(53.9)" font-size="100" text-anchor="middle" textLength="220" lengthAdjust="spacingAndGlyphs">70/30</text>
  <text class="on-band headline" transform="translate(234,376) rotate(53.9)" font-size="66" text-anchor="middle" textLength="720" lengthAdjust="spacingAndGlyphs">Upscale Reggae Soiree.</text>

  <text class="on-band mix" transform="translate(569,714) rotate(53.9)" font-size="28" text-anchor="middle" textLength="120" lengthAdjust="spacingAndGlyphs">70% Reggae</text>
  <text class="on-band mix" transform="translate(543,814) rotate(53.9)" font-size="28" text-anchor="middle" textLength="190" lengthAdjust="spacingAndGlyphs">30% Whatever Comes</text>

  <text class="on-green date" transform="translate(428,736) rotate(53.9)" font-size="28" text-anchor="middle" textLength="345" lengthAdjust="spacingAndGlyphs">Saturday May 4th, 10pm - 3am</text>
  <text class="on-green dress" transform="translate(340,689) rotate(53.9)" font-size="20" text-anchor="middle" textLength="150" lengthAdjust="spacingAndGlyphs">Dress to impress!</text>
  <text class="on-green dress" transform="translate(359,774) rotate(53.9)" font-size="18" text-anchor="middle" textLength="285" lengthAdjust="spacingAndGlyphs">We reserve the right to refuse entry</text>

  <text class="on-band tickets" transform="translate(497,251) rotate(-54)" font-size="24" text-anchor="middle" textLength="350" lengthAdjust="spacingAndGlyphs">Discounted Early Bird Online Tickets</text>
  <text class="on-band reservations" transform="translate(116,694) rotate(-54)" font-size="22" text-anchor="middle" textLength="330" lengthAdjust="spacingAndGlyphs">For Bottle Service Reservation:</text>
  <text class="on-band reservations" transform="translate(141,721) rotate(-54)" font-size="22" text-anchor="middle" textLength="320" lengthAdjust="spacingAndGlyphs">http://islandnights.ticketvoro.com</text>

  <text class="on-green venue" transform="translate(62,222) rotate(53.9)" font-size="24" text-anchor="middle" textLength="140" lengthAdjust="spacingAndGlyphs">The Copperloft:</text>
  <text class="on-green venue" transform="translate(109,350) rotate(53.9)" font-size="22" text-anchor="middle" textLength="300" lengthAdjust="spacingAndGlyphs">418 1/2 North Callow St, OKC</text>
  <text class="on-green guestlist" transform="translate(68,397) rotate(53.9)" font-size="24" text-anchor="middle" textLength="115" lengthAdjust="spacingAndGlyphs">Free Entry:</text>
  <text class="on-green guestlist" transform="translate(71,475) rotate(53.9)" font-size="24" text-anchor="middle" textLength="120" lengthAdjust="spacingAndGlyphs">1st 50 Ladies</text>
  <text class="on-green guestlist" transform="translate(70,544) rotate(53.9)" font-size="24" text-anchor="middle" textLength="135" lengthAdjust="spacingAndGlyphs">On VIP Guestlist</text>

  <text class="contact" x="258" y="800" font-size="40" text-anchor="middle" textLength="175" lengthAdjust="spacingAndGlyphs">More info?</text>
  <text class="contact" x="258" y="862" font-size="46" text-anchor="middle" textLength="235" lengthAdjust="spacingAndGlyphs">405-617-2958</text>
</svg>
</body>
</html>
```